Kelvo Auto - help to get me noticed

We not long ago tasked Pixel Harbour to design a logo for my business. I'm happy with the result so would like to have a business card designed as a follow up.

It's an Automotive service and repair business that offers the following -
- Servicing
- General repairs
- Brakes
- Detailing
- Integrity

Kelvo Automotive
Dallin Mereth
0471 926 317

Target Market(s)

Everyday people with the ability to reach out to corporate customers also.

Industry/Entity Type

Automotive

Contact Information for Business Card

Black card, logo, name and phone number on front. Other details on back of card.

```html
<!DOCTYPE html>
<html lang="en">
<head>
<meta charset="utf-8">
<title>Kelvo Automotive – Business Card</title>
<link href="https://fonts.googleapis.com/css2?family=Oswald:wght@300;500;600&family=Montserrat:wght@400&display=swap" rel="stylesheet">
<style>
  :root {
    --page-bg: #e6e6e6;
    --card-black: #111215;
    --pattern-dark: #141518;
    --pattern-light: #5a5b5e;
    --brand-green: #7dba2f;
    --text-white: #ffffff;
    --divider-grey: #8a8b8e;
  }
  html, body {
    margin: 0;
    padding: 0;
    width: 1200px;
    height: 960px;
    overflow: hidden;
    background: var(--page-bg);
  }
  .canvas {
    position: relative;
    width: 1200px;
    height: 960px;
  }
  .card {
    position: absolute;
    left: 321px;
    width: 566px;
    height: 346px;
    background: var(--card-black);
    overflow: hidden;
  }
  .card-front { top: 114px; }
  .card-back { top: 504px; }

  .front-pattern {
    position: absolute;
    inset: 0;
    background:
      radial-gradient(ellipse 260px 200px at 0% 0%, var(--pattern-light), transparent 75%),
      linear-gradient(125deg, #3a3b3e 0%, var(--pattern-dark) 38%, #1a1b1e 100%);
  }
  .brand-name {
    position: absolute;
    left: 0;
    right: 0;
    top: 148px;
    text-align: center;
    font-family: "Oswald", sans-serif;
    font-weight: 600;
    font-size: 40px;
    letter-spacing: 1px;
    color: var(--brand-green);
    margin: 0;
    line-height: 1;
  }

  .contact-line {
    position: absolute;
    left: 0;
    right: 0;
    top: 158px;
    display: flex;
    justify-content: center;
    align-items: center;
    font-family: "Oswald", sans-serif;
    line-height: 1;
  }
  .contact-name {
    font-weight: 500;
    font-size: 22px;
    color: var(--brand-green);
    letter-spacing: 0.2px;
  }
  .contact-divider {
    width: 2px;
    height: 28px;
    background: var(--brand-green);
    margin: 0 8px 0 9px;
  }
  .contact-phone {
    font-weight: 300;
    font-size: 19px;
    color: var(--text-white);
    letter-spacing: 3px;
  }

  .services {
    position: absolute;
    left: 0;
    right: 0;
    top: 300px;
    margin: 0;
    padding: 0;
    list-style: none;
    display: flex;
    justify-content: center;
    font-family: "Montserrat", sans-serif;
    font-size: 15px;
    color: var(--text-white);
    line-height: 1;
  }
  .services li + li::before {
    content: "|";
    margin: 0 5px;
    color: var(--divider-grey);
  }
  .services li.accent-sep::before { color: var(--brand-green); }
</style>
</head>
<body>
<main class="canvas">
  <section class="card card-front">
    <div class="front-pattern" role="img" aria-label="Repeating brand wordmark pattern on black, fading to silver at the top left"></div>
    <h1 class="brand-name">KELVO AUTOMOTIVE</h1>
  </section>

  <section class="card card-back">
    <div class="contact-line">
      <span class="contact-name">DALLIN MERETH</span>
      <span class="contact-divider"></span>
      <span class="contact-phone">0471 926 317</span>
    </div>
    <ul class="services">
      <li>Servicing</li>
      <li>General repairs</li>
      <li class="accent-sep">Brakes</li>
      <li>Detailing</li>
      <li class="accent-sep">Integrity</li>
    </ul>
  </section>
</main>
</body>
</html>
```